A-Stand Directional Sign Design

Objective:
We need a professional graphic design for an A-Stand sign that will guide customers arriving in our parking lot to our office. The design should be visually clear, welcoming, and aligned with our brand identity.
REQUIREMENTS:
Two versions of the design:
- One with an arrow pointing left
- One with an arrow pointing right
(This allows us to place the A-Stand anywhere and flip the graphic as needed.)
DIMENSIONS:
- Viewable Area: 30" x 40"
BRAND ALIGNMENT:
- Colors, fonts, and overall style should match our website: www.skornabel.com
- Clean, modern, and professional look consistent with our aviation/tourism brand
CONTENT:
- Clear directional arrow (left or right depending on version)
- Text: “Office Entrance” or similar concise wording (designers may propose alternatives if they improve clarity)
READABILITY:
- Bold, high-contrast design for visibility from a distance
- Simple layout that avoids clutter
DELIVERABLES:
- Final artwork in print-ready format (PDF preferred)
- Two versions: Arrow Left and Arrow Right
DESIGN GOAL:
Ensure customers can easily find our office upon arrival, while reinforcing skorNABEL’s professional and welcoming brand image.
Target Market(s)
Tourism

```html
<!DOCTYPE html>
<html lang="en">
<head>
<meta charset="UTF-8">
<title>skorNABEL – Office Entrance A-Stand</title>
<link rel="stylesheet" href="https://fonts.googleapis.com/css2?family=Montserrat:wght@600;800&display=swap">
<style>
  :root {
    --backdrop: #b4d4f6;
    --paper: #ffffff;
    --brand-blue: #458dc8;
    --brand-light: #a8c4e4;
    --ink-white: #ffffff;
  }
  html, body {
    margin: 0;
    padding: 0;
    width: 1200px;
    height: 1200px;
    overflow: hidden;
    background: var(--backdrop);
  }
  .sign {
    position: absolute;
    left: 225px;
    top: 100px;
    width: 750px;
    height: 1000px;
    background: var(--paper);
    overflow: hidden;
    box-shadow: 0 18px 40px rgba(40, 80, 140, 0.25);
  }
  .sign__brand {
    position: absolute;
    left: 0;
    right: 0;
    top: 0;
    height: 460px;
    display: flex;
    align-items: center;
    justify-content: center;
    gap: 22px;
  }
  .sign__brand-dot {
    width: 46px;
    height: 46px;
    border-radius: 50%;
    background: var(--brand-blue);
  }
  .sign__brand-name {
    font-family: "Montserrat", sans-serif;
    font-weight: 600;
    font-size: 86px;
    letter-spacing: 1px;
    color: var(--brand-blue);
  }
  .sign__divider {
    position: absolute;
    left: 0;
    right: 0;
    top: 460px;
    height: 22px;
    background: var(--brand-light);
  }
  .sign__panel {
    position: absolute;
    left: 0;
    right: 0;
    top: 482px;
    bottom: 0;
    background: var(--brand-blue);
  }
  .sign__message {
    position: absolute;
    left: 92px;
    top: 70px;
    margin: 0;
    font-family: "Montserrat", sans-serif;
    font-weight: 800;
    font-size: 100px;
    line-height: 1.04;
    letter-spacing: 2px;
    font-kerning: none;
    font-feature-settings: "kern" 0, "liga" 0;
    text-rendering: geometricPrecision;
    white-space: nowrap;
    color: var(--ink-white);
    text-transform: uppercase;
  }
  .sign__message-line {
    display: block;
  }
  .sign__arrow {
    position: absolute;
    left: 110px;
    top: 300px;
    width: 540px;
    height: 170px;
  }
</style>
</head>
<body>
  <main class="sign">
    <header class="sign__brand">
      <span class="sign__brand-dot"></span>
      <span class="sign__brand-name">skorNABEL</span>
    </header>
    <div class="sign__divider"></div>
    <section class="sign__panel">
      <h1 class="sign__message">
        <span class="sign__message-line">Office</span>
        <span class="sign__message-line">Entrance</span>
      </h1>
      <svg class="sign__arrow" viewBox="0 0 540 170" aria-label="Arrow pointing right">
        <polygon points="0,55 410,55 410,0 540,85 410,170 410,115 0,115" fill="var(--brand-light)"/>
      </svg>
    </section>
  </main>
</body>
</html>
```